Business Card Design - Carrington Hill Lodge

We are looking at a new design for our business cards that has a modern and professional look. We run a residential aged care facility focussing on the care of residents. The cards will be used for potential clients, consultants and business opportunities in this sector. Blue and white is our main colours and would to see these colours incorporated in the design.
Industry/Entity Type
Business
Contact Information for Business Card
Carrington Hill Lodge, Darren Pelham, dpelham@carringtonhilllodge.com.au, Finance Manager, 0491 736 208, BCom, 48 Yarrabee Way, Brookvale Heights, Qld 4199.

```html
<!DOCTYPE html>
<html lang="en">
<head>
<meta charset="utf-8">
<title>Carrington Hill Lodge – Business Card</title>
<link rel="stylesheet" href="https://fonts.googleapis.com/css2?family=Arvo:wght@400;700&display=swap">
<style>
  :root {
    --sky: #2cb5dc;
    --band: #3e6e85;
    --teal: #2aa3bd;
    --teal-deep: #1b8ea3;
    --paper: #f7f7f7;
    --paper-edge: #e6e6e6;
    --ink: #1c2a33;
    --ink-soft: #3b4a53;
    --mark: #c9ced6;
    --stage: #e4e7ea;
  }
  * { box-sizing: border-box; margin: 0; padding: 0; }
  html, body {
    width: 1200px; height: 800px; overflow: hidden;
    background: var(--stage);
    font-family: "Arvo", Georgia, serif;
  }
  .card {
    position: absolute;
    width: 525px; height: 300px;
    border-radius: 18px;
    overflow: hidden;
    box-shadow: 0 10px 28px rgba(0,0,0,.18);
  }
  .card svg.shape { position: absolute; inset: 0; }

  /* back of card */
  .card--back { left: 60px; top: 250px; background: var(--sky); }
  .back-mark {
    position: absolute; left: 50%; top: 50%;
    width: 132px; height: 132px; margin: -66px 0 0 -66px;
    border-radius: 50%;
    background: var(--band);
    border: 3px solid var(--sky);
    display: flex; align-items: center; justify-content: center;
    text-align: center;
  }
  .back-mark .brand-name {
    color: #ffffff; font-size: 14px; line-height: 1.35; font-weight: 700;
    letter-spacing: .04em; text-transform: uppercase;
  }

  /* front of card */
  .card--front { left: 615px; top: 250px; background: linear-gradient(135deg, #ffffff 0%, var(--paper) 60%, var(--paper-edge) 100%); }
  .holder {
    position: absolute; right: 34px; top: 28px; text-align: right; color: var(--ink);
  }
  .holder-name { font-size: 18px; font-weight: 700; }
  .holder-name .post { font-size: 14px; font-weight: 400; }
  .holder-role { font-size: 14px; color: var(--ink-soft); margin-top: 2px; }

  .front-mark {
    position: absolute; left: 200px; top: 92px;
    display: flex; align-items: center; gap: 10px;
  }
  .front-mark .dot { width: 38px; height: 38px; border-radius: 50%; background: var(--mark); }
  .front-mark .brand-name {
    color: var(--mark); font-size: 15px; font-weight: 700;
    letter-spacing: .06em; text-transform: uppercase; line-height: 1.2;
  }

  .phone {
    position: absolute; left: 30px; top: 148px;
    display: flex; align-items: center; gap: 10px;
    font-size: 17px; font-weight: 700; color: var(--ink);
  }
  .contact-band {
    position: absolute; left: 30px; bottom: 14px;
    font-size: 13px; color: var(--ink); line-height: 1.85;
  }
  .contact-band li { list-style: none; display: flex; align-items: center; gap: 10px; white-space: nowrap; }
  .icon { width: 14px; height: 14px; flex: none; fill: var(--ink); }
</style>
</head>
<body>

<section class="card card--back" aria-label="Business card, back">
  <svg class="shape" viewBox="0 0 525 300" aria-hidden="true">
    <polygon points="335,0 470,0 190,300 55,300" fill="var(--band)"/>
  </svg>
  <div class="back-mark">
    <span class="brand-name">Carrington<br>Hill Lodge</span>
  </div>
</section>

<section class="card card--front" aria-label="Business card, front">
  <svg class="shape" viewBox="0 0 525 300" aria-hidden="true">
    <path d="M402,168 H525 V214 H388 Q378,214 382,205 L392,176 Q395,168 402,168 Z" fill="var(--teal-deep)"/>
    <path d="M0,232 H318 Q326,232 334,226 L348,216 Q356,210 366,210 H525 V300 H0 Z" fill="var(--teal)"/>
  </svg>

  <header class="holder">
    <p class="holder-name">Darren Pelham, <span class="post">BCom.</span></p>
    <p class="holder-role">Finance Manager</p>
  </header>

  <div class="front-mark">
    <span class="dot"></span>
    <span class="brand-name">Carrington<br>Hill Lodge</span>
  </div>

  <p class="phone">
    <svg class="icon" viewBox="0 0 24 24" aria-hidden="true"><path d="M6.6 10.8a15.1 15.1 0 0 0 6.6 6.6l2.2-2.2a1 1 0 0 1 1-.25 11.4 11.4 0 0 0 3.6.57 1 1 0 0 1 1 1V20a1 1 0 0 1-1 1A17 17 0 0 1 3 4a1 1 0 0 1 1-1h3.5a1 1 0 0 1 1 1c0 1.25.2 2.45.57 3.57a1 1 0 0 1-.25 1z"/></svg>
    0491 736 208
  </p>

  <ul class="contact-band">
    <li>
      <svg class="icon" viewBox="0 0 24 24" aria-hidden="true"><path d="M2 5h20v14H2z M2 5l10 8 10-8" fill="none" stroke="var(--ink)" stroke-width="2.4"/></svg>
      dpelham@carringtonhilllodge.com.au
    </li>
    <li>
      <svg class="icon" viewBox="0 0 24 24" aria-hidden="true"><path d="M12 2a7 7 0 0 0-7 7c0 5.2 7 13 7 13s7-7.8 7-13a7 7 0 0 0-7-7zm0 9.5A2.5 2.5 0 1 1 12 6.5a2.5 2.5 0 0 1 0 5z"/></svg>
      48 Yarrabee Way, Brookvale Heights, Qld 4199
    </li>
  </ul>
</section>

</body>
</html>
```